Unique and original Business Card for Financial Services Business

I have moved premises and need to change the detail on my business card so thought now is a good time for a re-design. Looking for something professional and modern with colours to fit in with out logo. Like the idea of foil or embossing if that works but not a must have but I do want something that stands out and that I could not design myself.

Once business card is designed I will also be looking to get letterhead and flyers done but want the business card concept in place first.

The majority of designs I am receiving are generic and template based. I am looking for something unique and original. We have some great design elements in our logo, think outside the box and show me something that stands out from the crowd.

Target Market(s)

Business Professionals

Industry/Entity Type

Finance

Contact Information for Business Card

Name: Delphine Moore Phone 0438 297 614 Address PO Box 7816 Ashvale NSW 2411 Email info@tidewellmoneyservices.example.com.au website www.tidewellmoneyservices.example.com.au

Font styles to use
Other font styles liked:
• Ralway

Requirements
Should not have
• No black backgrounds please

```html
<!DOCTYPE html>
<html lang="en">
<head>
<meta charset="utf-8">
<title>Tidewell Money Services – Business Card</title>
<link href="https://fonts.googleapis.com/css2?family=Raleway:wght@300;400;500&display=swap" rel="stylesheet">
<style>
  :root {
    --page: #e9ecec;
    --teal: #0a9a98;
    --teal-light: #17b3aa;
    --teal-deep: #035a74;
    --teal-dark: #04485e;
    --silver-light: #e4e6e8;
    --silver-dark: #8e9398;
    --white: #ffffff;
    --ink-soft: #6c7378;
    --badge-green: #a6c935;
  }
  * { margin: 0; padding: 0; box-sizing: border-box; }
  html, body {
    width: 1200px; height: 900px; overflow: hidden;
    background: var(--page);
    font-family: "Raleway", sans-serif;
  }
  .canvas { position: relative; width: 1200px; height: 900px; }

  .card {
    position: absolute;
    width: 560px; height: 320px;
    overflow: hidden;
    box-shadow: 0 10px 28px rgba(0,0,0,0.18);
  }

  /* Back of card */
  .card-back {
    left: 80px; top: 70px;
    background: radial-gradient(ellipse at 58% 42%, var(--teal-light) 0%, var(--teal) 35%, var(--teal-deep) 100%);
    display: flex; align-items: center; justify-content: center;
  }
  .brand { display: flex; align-items: center; gap: 14px; font-weight: 300; }
  .brand-mark { width: 34px; height: 34px; border-radius: 50%; flex: none; }
  .brand-name { font-size: 38px; letter-spacing: 1px; line-height: 1; text-transform: uppercase; }
  .brand-sub { font-size: 15px; letter-spacing: 7px; margin-top: 6px; }
  .card-back .brand { color: var(--white); }
  .card-back .brand-mark { background: var(--white); }

  /* Front of card */
  .card-front { left: 560px; top: 500px; background: var(--white); }
  .front-art { position: absolute; inset: 0; width: 560px; height: 320px; }

  .card-front .brand { position: absolute; left: 300px; top: 62px; color: var(--teal); }
  .card-front .brand-name { font-size: 28px; }
  .card-front .brand-sub { font-size: 12px; letter-spacing: 5px; }
  .card-front .brand-mark { width: 26px; height: 26px; background: var(--teal); }

  .accreditation {
    position: absolute; left: 470px; top: 150px;
    display: flex; flex-direction: column; align-items: center; gap: 6px;
  }
  .accreditation-badge {
    width: 54px; height: 54px; border-radius: 50%;
    border: 2px solid var(--ink-soft);
    display: flex; align-items: center; justify-content: center;
  }
  .accreditation-badge span { width: 30px; height: 30px; border-radius: 50%; background: var(--badge-green); }
  .accreditation-note { font-size: 7px; color: var(--ink-soft); text-align: center; line-height: 1.3; }

  .contact { position: absolute; left: 30px; top: 150px; color: var(--white); }
  .person-name { font-size: 21px; font-weight: 500; text-transform: uppercase; letter-spacing: 0.5px; }
  .person-role { font-size: 13px; font-weight: 400; margin-bottom: 14px; }
  .contact-list { list-style: none; font-size: 11.5px; font-weight: 400; }
  .contact-list li { display: flex; align-items: center; gap: 8px; line-height: 19px; }
  .contact-list svg { width: 11px; height: 11px; flex: none; }
  .contact-divider { border-top: 1px solid rgba(255,255,255,0.6); margin: 6px 0; width: 300px; }
  .contact-address { font-size: 12.5px; }
</style>
</head>
<body>
<main class="canvas">

  <section class="card card-back" aria-label="Business card, back">
    <div class="brand">
      <span class="brand-mark"></span>
      <div>
        <div class="brand-name">Tidewell</div>
        <div class="brand-sub">Money Services</div>
      </div>
    </div>
  </section>

  <section class="card card-front" aria-label="Business card, front">
    <svg class="front-art" viewBox="0 0 560 320" aria-hidden="true">
      <defs>
        <linearGradient id="tealBody" x1="0" y1="0" x2="1" y2="1">
          <stop offset="0" stop-color="#0d9d99"/>
          <stop offset="1" stop-color="#0a8f96"/>
        </linearGradient>
        <linearGradient id="silverBand" x1="0" y1="0" x2="1" y2="1">
          <stop offset="0" stop-color="#eef0f1"/>
          <stop offset="0.5" stop-color="#9ba0a5"/>
          <stop offset="1" stop-color="#d4d7da"/>
        </linearGradient>
        <linearGradient id="deepBand" x1="0" y1="0" x2="1" y2="0">
          <stop offset="0" stop-color="#0a8e96"/>
          <stop offset="1" stop-color="#03506a"/>
        </linearGradient>
      </defs>
      <rect width="560" height="320" fill="url(#tealBody)"/>
      <polygon points="140,0 245,0 300,60 230,75" fill="url(#deepBand)"/>
      <polygon points="230,75 300,60 560,250 560,280" fill="url(#deepBand)"/>
      <polygon points="215,52 300,60 560,250 545,262" fill="url(#silverBand)"/>
      <polygon points="245,0 560,0 560,250 300,60" fill="#ffffff"/>
    </svg>

    <div role="img" aria-label="Faint floral emblem with hummingbird decoration"
         style="position:absolute;left:40px;top:40px;width:210px;height:210px;border-radius:50%;background:rgba(255,255,255,0.12);"></div>

    <div class="brand">
      <span class="brand-mark"></span>
      <div>
        <div class="brand-name">Tidewell</div>
        <div class="brand-sub">Money Services</div>
      </div>
    </div>

    <div class="accreditation">
      <div class="accreditation-badge"><span></span></div>
      <div class="accreditation-note">BAS agent<br>24681357</div>
    </div>

    <div class="contact">
      <div class="person-name">Delphine Moore</div>
      <div class="person-role">Registered BAS Agent</div>
      <ul class="contact-list">
        <li>
          <svg viewBox="0 0 12 12"><path d="M3 1 L5 3 L4 4.5 Q5.5 7 7.5 8 L9 7 L11 9 L9.5 11 Q4 10 1 3 Z" fill="#fff"/></svg>
          0438 297 614
        </li>
        <li>
          <svg viewBox="0 0 12 12"><rect x="1" y="2.5" width="10" height="7" fill="none" stroke="#fff" stroke-width="1.2"/><path d="M1 2.5 L6 7 L11 2.5" fill="none" stroke="#fff" stroke-width="1.2"/></svg>
          info@tidewellmoneyservices.example.com.au
        </li>
        <li>
          <svg viewBox="0 0 12 12"><circle cx="6" cy="6" r="4.8" fill="none" stroke="#fff" stroke-width="1.2"/><path d="M1.2 6 H10.8 M6 1.2 Q3 6 6 10.8 M6 1.2 Q9 6 6 10.8" fill="none" stroke="#fff" stroke-width="1"/></svg>
          www.tidewellmoneyservices.example.com.au
        </li>
        <li class="contact-divider" aria-hidden="true"></li>
        <li class="contact-address">
          <svg viewBox="0 0 12 12"><path d="M6 11 Q1.5 6 2 4 A4 4 0 0 1 10 4 Q10.5 6 6 11 Z" fill="#fff"/><circle cx="6" cy="4.3" r="1.4" fill="#0a9a98"/></svg>
          PO Box 7816 Ashvale NSW 2411
        </li>
      </ul>
    </div>
  </section>

</main>
</body>
</html>
```